8.5 x 8.5 - HELOC Product Campaign

Home Equity Lines of Credit
are BACK!!!

* Up to 97.5% on Owner Occupied Properties
* 700 Minimum Scores
* Fund in only 2-3 weeks

Can be used for...
* Education Expense
* Bill Consolidation
* Home Improvement
* Investments

Call today for more information!
(800) 417-2960

Bluegate Lending Partners, Inc.
NMLS #381760
www.bluegatelendhub.com

```html
<!DOCTYPE html>
<html lang="en">
<head>
<meta charset="utf-8">
<title>Bluegate Lending Partners – HELOC Campaign</title>
<link rel="stylesheet" href="https://fonts.googleapis.com/css2?family=Montserrat:wght@400;500;700;800;900&display=swap">
<style>
  :root{
    --blue:#0b5c9e;
    --blue-deep:#0a4f8a;
    --navy:#0d3a66;
    --olive:#aca134;
    --gold:#b9a63c;
    --white:#ffffff;
    --photo-warm:#c9b8a6;
  }
  *{margin:0;padding:0;box-sizing:border-box}
  html,body{width:1200px;height:1200px;overflow:hidden;background:var(--white)}
  .flyer{position:relative;width:1200px;height:1200px;font-family:"Montserrat",sans-serif;color:var(--navy);overflow:hidden}
  .backdrop{position:absolute;inset:0}
  .headline{position:absolute;left:84px;top:62px;color:var(--white);font-weight:400;font-size:69px;line-height:70px;letter-spacing:1px}
  .headline strong{font-weight:900}
  .equal-housing{position:absolute;left:1080px;top:30px;width:86px;height:86px;border:6px solid var(--white);border-radius:4px}
  .uses{position:absolute;left:71px;top:702px;color:var(--white)}
  .uses-intro{font-size:22px;font-weight:400;margin-bottom:6px}
  .uses-list{list-style:none;font-size:29px;line-height:34.5px;font-weight:500}
  .uses-list li::before{content:"•";margin-right:12px}
  .features{position:absolute;left:50px;top:944px;width:356px}
  .feature{display:flex;align-items:center;gap:14px;padding:8px 0;font-weight:800;font-size:22px;line-height:27px;color:var(--navy);border-bottom:1px solid #6b6b6b}
  .feature:last-child{border-bottom:none}
  .feature em{font-style:normal;color:var(--gold)}
  .feature svg{flex:0 0 38px;width:38px;height:38px}
  .brand{position:absolute;left:455px;top:1030px;width:300px;display:flex;align-items:center;justify-content:center;gap:10px;font-weight:800;font-size:19px;color:var(--blue)}
  .brand-dot{width:22px;height:22px;border-radius:50%;background:var(--olive)}
  .contact{position:absolute;left:783px;top:915px;width:380px}
  .call-pill{background:var(--navy);color:var(--white);border-radius:14px;height:28px;font-size:16px;font-weight:500;text-align:center;line-height:28px;letter-spacing:.3px}
  .phone-row{display:flex;align-items:center;gap:10px;margin-top:20px}
  .phone-number{font-size:40px;font-weight:500;color:var(--navy);letter-spacing:.5px}
  .website{margin-top:0;text-align:right;padding-right:22px;font-size:19px;font-weight:800;color:var(--gold)}
  .footer{position:absolute;left:0;top:1154px;width:1200px;height:34px;display:flex;font-size:16px;color:var(--white)}
  .footer-name{width:406px;background:var(--olive);font-weight:800;padding-left:72px;line-height:34px;font-size:17px}
  .footer-info{flex:1;background:var(--blue);display:flex;align-items:center;padding-left:34px;gap:16px;font-weight:500}
  .footer-sep{width:1px;height:24px;background:var(--white)}
</style>
</head>
<body>
<main class="flyer">
  <svg class="backdrop" width="1200" height="1200" viewBox="0 0 1200 1200">
    <defs>
      <linearGradient id="bluePhoto" x1="0" y1="0" x2="1" y2="1">
        <stop offset="0" stop-color="#0d66aa"/>
        <stop offset="1" stop-color="#0a4f8a"/>
      </linearGradient>
      <linearGradient id="warmPhoto" x1="0" y1="0" x2="1" y2="1">
        <stop offset="0" stop-color="#d9cfc4"/>
        <stop offset="1" stop-color="#8e6e58"/>
      </linearGradient>
      <linearGradient id="gradPhoto" x1="0" y1="0" x2="0" y2="1">
        <stop offset="0" stop-color="#a7a18a"/>
        <stop offset="1" stop-color="#1e2536"/>
      </linearGradient>
    </defs>
    <path d="M0 0H1200V402L1080 500L0 271Z" fill="url(#bluePhoto)" role="img" aria-label="Blue-tinted photo of a smiling couple relaxing at home"/>
    <path d="M1200 402V529L1090 610V480Z" fill="var(--olive)"/>
    <path d="M0 271L420 560L600 860Q300 935 0 880Z" fill="var(--olive)"/>
    <ellipse cx="833" cy="624" rx="344" ry="351" fill="var(--white)"/>
    <ellipse cx="833" cy="624" rx="335" ry="342" fill="url(#warmPhoto)" role="img" aria-label="Photo of a couple reviewing loan paperwork together at a table"/>
    <circle cx="140" cy="454" r="151" fill="var(--white)"/>
    <circle cx="140" cy="454" r="142" fill="#d8cfc6" role="img" aria-label="Photo of a couple choosing flooring samples for a renovation"/>
    <circle cx="458" cy="540" r="200" fill="var(--white)"/>
    <circle cx="458" cy="540" r="191" fill="url(#gradPhoto)" role="img" aria-label="Photo of a smiling graduate in cap and gown holding a diploma"/>
    <circle cx="915" cy="237" r="185" fill="var(--white)"/>
    <circle cx="915" cy="237" r="176" fill="#c7bfb8" role="img" aria-label="Photo of a couple holding painting tools during home improvement"/>
  </svg>

  <h1 class="headline">HOME EQUITY<br>LINES OF CREDIT<br>ARE <strong>BACK!!!</strong></h1>

  <div class="equal-housing" role="img" aria-label="Equal housing badge"></div>

  <section class="uses">
    <p class="uses-intro">Can be used for...</p>
    <ul class="uses-list">
      <li>Education Expense</li>
      <li>Bill Consolidation</li>
      <li>Home Improvement</li>
      <li>Investments</li>
    </ul>
  </section>

  <section class="features">
    <div class="feature">
      <svg viewBox="0 0 38 38" fill="none" stroke="var(--gold)" stroke-width="2.5"><path d="M8 18L19 8L30 18M11 16V26H27V16"/><path d="M3 30Q12 26 19 30L33 27" stroke-linecap="round"/></svg>
      <span>Up to <em>97.5%</em> on Owner Occupied Properties</span>
    </div>
    <div class="feature">
      <svg viewBox="0 0 38 38" fill="none" stroke="var(--gold)" stroke-width="2.5"><rect x="8" y="6" width="22" height="28" rx="2"/><path d="M14 4H24V9H14Z M12 15H16M20 15H26M12 21H16M20 21H26M12 27H16M20 27H26"/></svg>
      <span><em>700</em> Minimum Scores</span>
    </div>
    <div class="feature">
      <svg viewBox="0 0 38 38" fill="none" stroke="var(--gold)" stroke-width="2.5"><rect x="4" y="7" width="30" height="27" rx="2"/><path d="M4 14H34M12 3V10M26 3V10M10 20H14M17 20H21M24 20H28M10 26H14M17 26H21M24 26H28"/></svg>
      <span>Fund in only <em>2-3</em> weeks</span>
    </div>
  </section>

  <div class="brand"><span class="brand-dot"></span><span>Bluegate Lending Partners, Inc.</span></div>

  <section class="contact">
    <div class="call-pill">CALL TODAY FOR MORE INFORMATION!</div>
    <div class="phone-row">
      <svg width="54" height="58" viewBox="0 0 54 58"><rect x="18" y="2" width="30" height="52" rx="5" fill="var(--navy)"/><rect x="22" y="9" width="22" height="34" fill="var(--white)"/><circle cx="33" cy="48" r="2.5" fill="var(--white)"/><path d="M4 30Q4 22 12 20L22 18V44Q10 50 4 40Z" fill="var(--navy)"/></svg>
      <span class="phone-number">(800) 417-2960</span>
    </div>
    <div class="website">www.bluegatelendhub.com</div>
  </section>

  <footer class="footer">
    <div class="footer-name">Bluegate Lending Partners, Inc.</div>
    <div class="footer-info">
      <span>
        <svg width="10" height="14" viewBox="0 0 10 14" fill="none" stroke="var(--white)" stroke-width="1.5"><path d="M5 13C2 9 1 7 1 5A4 4 0 0 1 9 5C9 7 8 9 5 13Z"/><circle cx="5" cy="5" r="1.5"/></svg>
        MARYLAND OFFICE: 2180 Harlow Creek Rd, Fairbrook, MD 21099
      </span>
      <span class="footer-sep"></span>
      <span>NMLS #381760</span>
    </div>
  </footer>
</main>
</body>
</html>
```